Catalogue for Eco friendly products

HI We have 2 brands - logos attached
Lumatotesnz
Brimwrap

We would like a catalog of these products :

Size of the catalogue: A4 Size

Lumatotes - ( www.lumatotes.co.nz)
Cotton bags
Canvas bags
Jute bags
Non woven bags
Tindlewag poop bags

Brimwrap
Degradable bin liners
Compostable bin liners
Recycled bin liners
Paper bags
Customised packaging

All products need to be on A4 page which can be inserted in a folder, the main reason for that to make sales presentation as per the customer requirement. All customers don't need all the products.

We are looking for the designer to make a clean feel where both the logos sit comfortably with each other.

We will need 2 main designs:
1 will be the outside folder design
Inside Catalog for the products with place holders for the photographs and words which can be limited to 10-20 words to ensure that design looks uniform. All products are on our website to provide you with an idea of what we are looking for.

Brimwrap packaging logo is included for your reference to get a feel of the products.
Any other information please let me know.
Thanks

Target Market(s)

B2B- Businesses , purchase manager , event managers, Organic shop owners

Font styles to use
Serif
Sans Serif

Colors
add136
abd037
acd037
cadf82
9bcb3c
f37122

Requirements
Must have
• A Clean design and yet interesting , use of green colour is preferred for the design but complimentary earthy colors are ok
• TEXT in design: Attached for 1 product category : Cotton
Nice to have
• Please see the design inspirations which I like. Please note that these are just to give you an idea of what kind of design we would prefer and is to be used as our guidance to you.

```html
<!DOCTYPE html>
<html lang="en">
<head>
<meta charset="utf-8">
<title>Lumatotesnz Catalogue Spread</title>
<link rel="stylesheet" href="https://fonts.googleapis.com/css2?family=Bitter:wght@700&family=Open+Sans:wght@400;600&display=swap">
<style>
  :root {
    --lime: #add136;
    --lime-bright: #b7dc2c;
    --lime-soft: #cadf82;
    --lime-deep: #9bcb3c;
    --white: #ffffff;
    --canvas-bg: #f1eee8;
    --strip: #ffffff;
  }
  * { box-sizing: border-box; margin: 0; padding: 0; }
  html, body { width: 1200px; height: 1200px; overflow: hidden; }
  body { background: var(--canvas-bg); position: relative; font-family: "Open Sans", sans-serif; }

  .spread { position: absolute; left: 200px; width: 800px; height: 560px; display: flex; box-shadow: 0 6px 18px rgba(0,0,0,.15); }
  .spread--intro { top: 20px; }
  .spread--products { top: 620px; }
  .page { position: relative; width: 400px; height: 560px; overflow: hidden; }
  .page--green {
    background:
      radial-gradient(ellipse 70% 50% at 45% 30%, rgba(214,240,120,.55) 0%, rgba(214,240,120,0) 70%),
      radial-gradient(ellipse 60% 40% at 50% 85%, rgba(214,240,120,.35) 0%, rgba(214,240,120,0) 70%),
      linear-gradient(180deg, var(--lime-bright), var(--lime));
  }

  .hero-photo {
    position: absolute; inset: 0;
    background:
      radial-gradient(circle at 45% 48%, #4f7d23 0%, #33601a 18%, rgba(51,96,26,0) 40%),
      radial-gradient(ellipse at 70% 20%, #9cc24a 0%, rgba(156,194,74,0) 55%),
      linear-gradient(160deg, #6f9a33 0%, #2f4f16 55%, #6c8e2c 100%);
  }

  .about { padding: 34px 34px 0 36px; color: var(--white); }
  .about__title { font-family: "Bitter", serif; font-weight: 700; font-size: 28px; text-align: center; margin-bottom: 22px; letter-spacing: .5px; }
  .about__text { font-family: "Bitter", serif; font-weight: 700; font-size: 11px; line-height: 1.55; text-align: justify; margin-bottom: 14px; }

  .product-list { position: absolute; left: 26px; top: 22px; width: 250px; color: var(--white); }
  .page--right .product-list { left: 18px; }
  .product { height: 104px; }
  .product__name { font-size: 21px; font-weight: 400; line-height: 1.2; margin-bottom: 4px; }
  .product__desc { font-size: 8.5px; line-height: 1.55; }

  .thumb-strip { position: absolute; top: 0; bottom: 0; width: 92px; background: var(--strip); display: flex; flex-direction: column; justify-content: space-around; align-items: center; padding: 14px 0; }
  .page--left .thumb-strip { right: 6px; }
  .page--right .thumb-strip { right: 34px; }
  .thumb { width: 56px; height: 74px; border-radius: 3px; }
  .thumb--cotton { background: linear-gradient(#f7f4ea, #e6e0cc); }
  .thumb--canvas { background: linear-gradient(135deg, #f3f0ee, #d9b9c9); }
  .thumb--jute { background: linear-gradient(#d9c08d, #b99a5c); }
  .thumb--nonwoven { background: linear-gradient(135deg, #5bbf3a, #e24a6a); }
  .thumb--poop { background: linear-gradient(135deg, #e86aa6, #8cc63f); }
  .thumb--degradable { background: linear-gradient(#2a2a2a, #111); }
  .thumb--compostable { background: linear-gradient(135deg, #39b54a, #1f7f2f); }
  .thumb--recycled { background: radial-gradient(circle at 40% 35%, #444, #0d0d0d); }
  .thumb--paper { background: linear-gradient(#c9a86a, #a88446); }
  .thumb--custom { background: linear-gradient(#f3ede0, #dccfb3); }
</style>
</head>
<body>

<section class="spread spread--intro">
  <div class="page page--left">
    <div class="hero-photo" role="img" aria-label="Close-up photograph of an unfurling green fern frond against a soft green background"></div>
  </div>
  <div class="page page--right page--green">
    <div class="about">
      <h1 class="about__title">ABOUT US</h1>
      <p class="about__text">Lumatotesnz™ is a growing New Zealand-based business whose mission is to provide an eco-friendly alternative to plastic bags and give customers a smarter, more sustainable packaging choice.</p>
      <p class="about__text">Lumatotesnz was started 10 years ago by a husband and wife team who established a niche in B2B market for providing reusable bags. Supported by a close-knit team with experience in all facets of design and production enables us to deliver quality product to our customers.</p>
      <p class="about__text">We supply bags made from jute, cotton, canvas, non-woven fabrics directly imported from overseas with our production facility in India which is FairHands certified, ISO Certified and ETHIQA certified. Our strong suppliers relationship in Asia and our own warehouse and storage facilities help us to provide an end to end solution to our customers.</p>
      <p class="about__text">We make the process simple and hassle-free for our clients as we take the time to understand their business needs. Our satisfied clients who come back for repeat orders are a testament to the exceptional work we do. Our customers range across different sectors such as Halden Apparel, Corvex Power, Orvalle TV, Puregrove and Civic Records Office to name a few.</p>
    </div>
  </div>
</section>

<section class="spread spread--products">
  <div class="page page--left page--green">
    <div class="product-list">
      <article class="product">
        <h2 class="product__name">Cotton bags</h2>
        <p class="product__desc">Calico is made from unbleached 100% cotton. These bags are an eco-friendly, economically priced packaging which will present your product attractively, displaying your brand and message to your exact specification.</p>
      </article>
      <article class="product">
        <h2 class="product__name">Canvas bags</h2>
        <p class="product__desc">Canvas is a thick, heavy grade cotton designed for heavy duty usage, durability and carrying heavy products. Canvas bags have multiple uses and can be used as tote bags, string bags, produce bags, and gift bags.</p>
      </article>
      <article class="product">
        <h2 class="product__name">Jute bags</h2>
        <p class="product__desc">Welcome to LumatotesNZ's Jute Bag collection! We showcase a wide range of colourful jute, burlap and hemp conference bags and totes we think you're gonna love!</p>
      </article>
      <article class="product">
        <h2 class="product__name">Non woven bags</h2>
        <p class="product__desc">Non-woven Polypropylene (NWPP) is man-made and manufactured using light-weight polymers. The end product is immensely strong and durable.</p>
      </article>
      <article class="product">
        <h2 class="product__name">Tindlewag poop Bags</h2>
        <p class="product__desc">We are the distributors for Tindlewag PoopBags in New Zealand. While we love pups, picking up the poop ain't so much flash! Luckily our range of bags make picking up poop a little more fun – all while keeping your pocketbook happy.</p>
      </article>
    </div>
    <div class="thumb-strip">
      <div class="thumb thumb--cotton" role="img" aria-label="Product photo of a white cotton tote bag"></div>
      <div class="thumb thumb--canvas" role="img" aria-label="Product photo of a printed canvas tote bag"></div>
      <div class="thumb thumb--jute" role="img" aria-label="Product photo of a jute tote bag"></div>
      <div class="thumb thumb--nonwoven" role="img" aria-label="Product photo of a colourful printed non woven bag"></div>
      <div class="thumb thumb--poop" role="img" aria-label="Product photo of dog poop bag packs and dispenser"></div>
    </div>
  </div>

  <div class="page page--right page--green">
    <div class="product-list">
      <article class="product">
        <h2 class="product__name">Degradable bin liners</h2>
        <p class="product__desc">Calvexa manufactures the Degradable additive called KDPA, which helps the bag to break down in circumstances where the bag is exposed to natural UV light, heat and oxygen (for example, if the bag becomes litter).</p>
      </article>
      <article class="product">
        <h2 class="product__name">Compostable bin liners</h2>
        <p class="product__desc">Lumatotes NZ compostable liners are made from renewable plant starch, helping you to step away from plastic by switching today.</p>
      </article>
      <article class="product">
        <h2 class="product__name">Recycled bin liners</h2>
        <p class="product__desc">Welcome to our recycled liner range. We showcase a wide choice of sizes for office, home and conference use.</p>
      </article>
      <article class="product">
        <h2 class="product__name">Paper bags</h2>
        <p class="product__desc">Whether for retail or takeaway, you'll find strong kraft paper bags in every size at Lumatotes.</p>
      </article>
      <article class="product">
        <h2 class="product__name">Customised packaging</h2>
        <p class="product__desc">Whether you need a thousand paper bags or just a few, you'll find what you want in our huge selection here at Lumatotes!</p>
      </article>
    </div>
    <div class="thumb-strip">
      <div class="thumb thumb--degradable" role="img" aria-label="Product photo of a black degradable bin liner pack"></div>
      <div class="thumb thumb--compostable" role="img" aria-label="Product photo of a green roll of compostable bin liners"></div>
      <div class="thumb thumb--recycled" role="img" aria-label="Product photo of a filled black recycled bin liner"></div>
      <div class="thumb thumb--paper" role="img" aria-label="Product photo of a brown kraft paper bag"></div>
      <div class="thumb thumb--custom" role="img" aria-label="Product photo of small calico drawstring pouches"></div>
    </div>
  </div>
</section>

</body>
</html>
```